Classy business card for accounting firm

We're looking for a new business card for our accounting firm. Our logo was designed by Brandolith, so all of the design info we would like to use has been provided. The specific font provided isn't required to be used.

We want the card to look classy and elegent. Probably more minimalistic, but still with some pops of color.

The options we would like to include on the card are as follows:
1. Main office phone line
2. Direct phone line
3. Email address
4. Website URL
5. Name
6. Title (CEO, President, etc.)
7. Firm Address

The design and card should be double sided!!! The drop down box in the project brief for some reason is defaulting to single sided. Not sure why this is happening.

Thanks!

Contact Information for Business Card

The options we would like to include on the card are as follows: 1. Main office phone line 2. Direct phone line 3. Email address 4. Website URL 5. Name 6. Title (CEO, President, etc.) 7. Firm Address

Requirements
Must have
• Card must be double sided.

```html
<!DOCTYPE html>
<html lang="en">
<head>
<meta charset="UTF-8">
<title>Kellbrook – Business Card</title>
<link href="https://fonts.googleapis.com/css2?family=Montserrat:wght@400;500;600;700&display=swap" rel="stylesheet">
<style>
  :root {
    --backdrop: #9c9c9c;
    --paper: #f7f7f6;
    --ink: #5d5d5d;
    --ink-soft: #7a7a7a;
    --accent: #ee8128;
    --rule: #8a8a8a;
    --card-dark: #3c3c3c;
    --card-dark-edge: #2e2e2e;
    --mark-dark: #262626;
  }
  * { box-sizing: border-box; margin: 0; padding: 0; }
  html, body {
    width: 1200px;
    height: 1000px;
    overflow: hidden;
  }
  body {
    background: var(--backdrop);
    font-family: "Montserrat", Arial, sans-serif;
    display: flex;
    flex-direction: column;
    align-items: center;
    justify-content: center;
    gap: 60px;
  }
  .card {
    position: relative;
    width: 700px;
    height: 400px;
    box-shadow: 0 10px 30px rgba(0, 0, 0, 0.25);
  }

  /* Front */
  .card--front {
    background: var(--paper);
    color: var(--ink);
  }
  .brand {
    position: absolute;
    display: flex;
    align-items: center;
    gap: 10px;
  }
  .card--front .brand {
    top: 56px;
    right: 52px;
  }
  .brand__dot {
    width: 14px;
    height: 14px;
    border-radius: 50%;
    background: var(--accent);
  }
  .brand__name {
    font-size: 24px;
    font-weight: 600;
    letter-spacing: 0;
    color: var(--ink);
  }
  .person {
    position: absolute;
    top: 116px;
    left: 52px;
  }
  .person__name {
    font-size: 26px;
    font-weight: 700;
    color: var(--accent);
    letter-spacing: 0.02em;
    line-height: 1.1;
  }
  .person__title {
    font-size: 15px;
    color: var(--ink-soft);
    margin-top: 2px;
  }
  .divider {
    position: absolute;
    top: 182px;
    left: 52px;
    right: 52px;
    height: 1px;
    background: var(--rule);
  }
  .contact {
    position: absolute;
    top: 196px;
    left: 52px;
    list-style: none;
  }
  .contact__item {
    display: flex;
    align-items: center;
    gap: 8px;
    font-size: 15px;
    line-height: 23px;
    color: var(--ink-soft);
  }
  .contact__icon {
    width: 12px;
    height: 12px;
    fill: var(--accent);
    flex: none;
  }
  .address {
    position: absolute;
    right: 52px;
    bottom: 30px;
    text-align: right;
    font-size: 15px;
    line-height: 21px;
    color: var(--ink-soft);
    font-style: normal;
  }
  .address__label {
    color: var(--accent);
    font-size: 16px;
  }

  /* Back */
  .card--back {
    background: linear-gradient(160deg, var(--card-dark-edge) 0%, var(--card-dark) 55%, #444 100%);
    display: flex;
    align-items: center;
    justify-content: center;
  }
  .card--back .brand {
    position: static;
  }
  .card--back .brand__dot {
    background: var(--mark-dark);
    width: 18px;
    height: 18px;
  }
  .card--back .brand__name {
    font-size: 32px;
    color: var(--mark-dark);
  }
</style>
</head>
<body>

  <section class="card card--front" aria-label="Business card, front">
    <div class="brand">
      <span class="brand__dot"></span>
      <span class="brand__name">Kellbrook</span>
    </div>

    <div class="person">
      <h1 class="person__name">NAME</h1>
      <p class="person__title">Title(CEO,President,etc)</p>
    </div>

    <div class="divider"></div>

    <ul class="contact">
      <li class="contact__item">
        <svg class="contact__icon" viewBox="0 0 24 24"><path d="M6.6 10.8a15.1 15.1 0 0 0 6.6 6.6l2.2-2.2a1 1 0 0 1 1-.25 11.4 11.4 0 0 0 3.6.57 1 1 0 0 1 1 1V20a1 1 0 0 1-1 1A17 17 0 0 1 3 4a1 1 0 0 1 1-1h3.5a1 1 0 0 1 1 1c0 1.25.2 2.45.57 3.57a1 1 0 0 1-.25 1z"/></svg>
        Main office phone line
      </li>
      <li class="contact__item">
        <svg class="contact__icon" viewBox="0 0 24 24"><path d="M7 1h10a2 2 0 0 1 2 2v18a2 2 0 0 1-2 2H7a2 2 0 0 1-2-2V3a2 2 0 0 1 2-2zm0 3v14h10V4z"/></svg>
        Direct phone
      </li>
      <li class="contact__item">
        <svg class="contact__icon" viewBox="0 0 24 24"><path d="M2 5h20v14H2zm2 2v.5l8 5 8-5V7z"/></svg>
        email address
      </li>
      <li class="contact__item">
        <svg class="contact__icon" viewBox="0 0 24 24"><path d="M12 2a10 10 0 1 0 0 20 10 10 0 0 0 0-20zm6.9 9h-3a15 15 0 0 0-1.4-6.1A8 8 0 0 1 18.9 11zM12 4c.9 1.2 1.8 3.6 1.9 7h-3.8c.1-3.4 1-5.8 1.9-7zM9.5 4.9A15 15 0 0 0 8.1 11h-3a8 8 0 0 1 4.4-6.1zM5.1 13h3a15 15 0 0 0 1.4 6.1A8 8 0 0 1 5.1 13zM12 20c-.9-1.2-1.8-3.6-1.9-7h3.8c-.1 3.4-1 5.8-1.9 7zm2.5-.9a15 15 0 0 0 1.4-6.1h3a8 8 0 0 1-4.4 6.1z"/></svg>
        websiteURL
      </li>
    </ul>

    <address class="address">
      <span class="address__label">Firm address</span><br>
      Address Line one,<br>
      City, State, Country
    </address>
  </section>

  <section class="card card--back" aria-label="Business card, back">
    <div class="brand">
      <span class="brand__dot"></span>
      <span class="brand__name">Kellbrook</span>
    </div>
  </section>

</body>
</html>
```